Naturopath Practitioner Card Design

I am a naturopath needing a design for a business card mainly to show that I am a naturopath and have some contact details to give to prospective clients. I am open minded about the design and what is on the second side of the card whether it just be some artwork or space for details, appointment times etc. Naturopathy is the practice of natural medicine that uses a holistic approach and incorporates herbal and nutritional medicine.

Industry/Entity Type

Business

Contact Information for Business Card

Tom Welby NaturopathBHSc (Naturopathy) Member PHRA 0492 815 306 tom.welby@mailbright.com www.tomwelbynaturopathy.com.au

Requirements
Nice to have
• Would prefer some kind of original pattern/art work/logo rather than an image, not fussed if its very simple/basic
• I am open to any colour but think I would prefer a more earthy sandy clay etc type style than the greens that are commonly associated with naturopathy.
Should not have
• Don't really want to have generic stock images on it

```html
<!DOCTYPE html>
<html lang="en">
<head>
<meta charset="utf-8">
<title>Tom Welby Naturopath – Business Card</title>
<link rel="stylesheet" href="https://fonts.googleapis.com/css2?family=Montserrat:wght@400;700&display=swap">
<style>
  :root {
    --page-bg: #ecebe8;
    --wood-light: #d9d9d9;
    --wood-mid: #bdbdbd;
    --wood-dark: #6f6f6f;
    --sage: #9cc18e;
    --sheet-white: rgba(255,255,255,0.55);
    --clay-brown: #8a7466;
    --ink: #2b2b2b;
  }
  * { margin: 0; padding: 0; box-sizing: border-box; }
  html, body {
    width: 1200px; height: 800px; overflow: hidden;
    background: var(--page-bg);
    font-family: "Montserrat", Arial, sans-serif;
  }
  .canvas {
    width: 1200px; height: 800px;
    display: flex; flex-direction: column; align-items: center; justify-content: center;
    gap: 40px;
  }
  .card {
    position: relative;
    width: 560px; height: 320px;
    overflow: hidden;
    box-shadow: 0 6px 18px rgba(0,0,0,0.18);
  }
  .card__art { position: absolute; inset: 0; width: 100%; height: 100%; }
  .wordmark {
    position: absolute;
    text-align: center;
    color: var(--clay-brown);
    font-weight: 400;
  }
  .wordmark__name { font-size: 34px; line-height: 1; letter-spacing: 0.5px; }
  .wordmark__role { font-size: 12px; margin-top: 4px; opacity: 0.9; }
  .card--front .wordmark { left: 230px; top: 128px; width: 230px; }
  .card--back .wordmark { left: 330px; top: 44px; width: 190px; }
  .card--back .wordmark__name { font-size: 28px; }
  .wordmark__dot {
    display: inline-block; width: 8px; height: 8px; border-radius: 50%;
    background: var(--clay-brown); margin-bottom: 8px;
  }
  .contact {
    position: absolute; left: 34px; bottom: 30px;
    color: var(--ink);
  }
  .contact__name { font-weight: 700; font-size: 18px; letter-spacing: 2px; }
  .contact__title { font-size: 13px; margin-top: 4px; letter-spacing: 0.5px; }
  .contact__lines { margin-top: 16px; font-size: 14px; line-height: 1.45; letter-spacing: 0.5px; }
</style>
</head>
<body>
<main class="canvas">

  <section class="card card--front" aria-label="Card front">
    <svg class="card__art" viewBox="0 0 560 320" preserveAspectRatio="none">
      <defs>
        <linearGradient id="woodFront" x1="0" y1="0" x2="1" y2="0">
          <stop offset="0" stop-color="#7a7a7a"/>
          <stop offset="0.45" stop-color="#9a9a9a"/>
          <stop offset="0.7" stop-color="#c9c9c9"/>
          <stop offset="1" stop-color="#dedede"/>
        </linearGradient>
      </defs>
      <rect width="560" height="320" fill="url(#woodFront)" role="img" aria-label="Grey weathered timber plank texture"/>
      <polygon points="0,0 200,0 20,320 0,320" fill="var(--sage)" opacity="0.85"/>
      <polygon points="60,0 560,0 560,40 90,320 0,320 0,180" fill="#5e5e5e" opacity="0.35"/>
      <polygon points="90,70 400,10 300,320" fill="var(--sheet-white)"/>
      <polygon points="100,170 420,40 470,200" fill="var(--sheet-white)"/>
      <polygon points="560,0 480,0 380,320 560,320" fill="#ffffff" opacity="0.3"/>
    </svg>
    <div class="wordmark">
      <span class="wordmark__dot"></span>
      <div class="wordmark__name">Tom Welby</div>
      <div class="wordmark__role">Naturopath</div>
    </div>
  </section>

  <section class="card card--back" aria-label="Card back">
    <svg class="card__art" viewBox="0 0 560 320" preserveAspectRatio="none">
      <rect width="560" height="320" fill="var(--wood-light)" role="img" aria-label="Pale whitewashed timber plank texture"/>
      <polygon points="40,40 180,40 560,250 560,310" fill="var(--wood-dark)" opacity="0.55"/>
      <polygon points="140,60 330,0 540,270" fill="var(--sheet-white)"/>
      <polygon points="60,50 300,100 500,300 300,300" fill="#ffffff" opacity="0.35"/>
    </svg>
    <div class="wordmark">
      <span class="wordmark__dot"></span>
      <div class="wordmark__name">Tom Welby</div>
      <div class="wordmark__role">Naturopath</div>
    </div>
    <div class="contact">
      <div class="contact__name">TOM WELBY</div>
      <div class="contact__title">Naturopath BHSc, Member PHRA</div>
      <div class="contact__lines">
        <div>0492 815 306</div>
        <div>tom.welby@mailbright.com</div>
      </div>
    </div>
  </section>

</main>
</body>
</html>
```